Solace Chiropractic & Acupuncture Business Cards

I need a business card design that feels elevated. I am open to any of the logo designs uploaded. We have two doctors so I'll need to be able to change out the names.

Information:
Marnie Toller D.C., Dipl. Ac. ASA
584 W 12th St, Ste 320
Marlow Bend, KS 67419
solacegrove.net
620-555-0147
drmarnie@solacegrove.com
Updates

We have designs we like now, we are just trying to choose between top contenders. Thanks for your submissions!

Contact Information for Business Card

noted in description

Requirements
Must have
• ability to edit info if possible
Nice to have
• Please see our website solacegrove.net for our style and colors

```html
<!DOCTYPE html>
<html lang="en">
<head>
<meta charset="utf-8">
<title>Solace Chiropractic &amp; Acupuncture — Business Card</title>
<link rel="stylesheet" href="https://fonts.googleapis.com/css2?family=Playfair+Display:wght@400;700&family=Montserrat:wght@400&display=swap">
<style>
  :root {
    --backdrop: #dededd;
    --card: #e2e3dd;
    --ink: #2f3a4f;
    --serif: "Playfair Display", Georgia, serif;
    --sans: "Montserrat", Arial, sans-serif;
  }
  * { box-sizing: border-box; margin: 0; padding: 0; }
  html, body {
    width: 1200px;
    height: 1124px;
    overflow: hidden;
    background: var(--backdrop);
  }
  .canvas { position: relative; width: 1200px; height: 1124px; }

  .card {
    position: absolute;
    left: 252px;
    width: 696px;
    height: 398px;
    background: var(--card);
    border-radius: 30px;
    overflow: hidden;
    color: var(--ink);
  }
  .card--front { top: 134px; }
  .card--back { top: 592px; }

  /* practice name: one family, one weight, one colour, plain stacked text */
  .practice-name {
    position: absolute;
    font-family: var(--serif);
    font-weight: 400;
    color: var(--ink);
    line-height: 1;
  }
  .practice-name__main { display: block; }
  .practice-name__sub { display: block; }

  .card--front .practice-name { left: 40px; top: 52px; }
  .card--front .practice-name__main { font-size: 52px; }
  .card--front .practice-name__sub { font-size: 17px; margin-top: 8px; }

  .card--back .practice-name { left: 0; right: 0; top: 128px; text-align: center; }
  .card--back .practice-name__main { font-size: 100px; }
  .card--back .practice-name__sub { font-size: 28px; margin-top: 14px; }

  .name-tab {
    position: absolute;
    left: 0; top: 192px;
    width: 22px; height: 57px;
    background: var(--ink);
    border-radius: 0 8px 8px 0;
  }
  .doctor { position: absolute; left: 40px; top: 186px; font-family: var(--serif); }
  .doctor__name { font-size: 31px; font-weight: 700; line-height: 34px; letter-spacing: 0.2px; }
  .doctor__credentials { font-size: 26px; font-weight: 400; line-height: 32px; }

  .contact { position: absolute; left: 40px; top: 280px; list-style: none; font-family: var(--sans); font-size: 15.5px; }
  .contact li { display: flex; align-items: center; height: 25.5px; }
  .contact svg { width: 12px; height: 12px; margin-right: 6px; fill: var(--ink); }

  .address {
    position: absolute;
    right: 40px; top: 309px;
    font-family: var(--sans);
    font-style: normal;
    font-size: 15.5px;
    line-height: 25px;
    text-align: right;
  }
  .accent-bar {
    position: absolute;
    left: 464px; bottom: 0;
    width: 192px; height: 12px;
    background: var(--ink);
  }
</style>
</head>
<body>
<main class="canvas">

  <section class="card card--front" aria-label="Card front">
    <div class="practice-name">
      <span class="practice-name__main">Solace</span>
      <span class="practice-name__sub">Chiropractic &amp; Acupuncture</span>
    </div>

    <div class="name-tab"></div>
    <div class="doctor">
      <p class="doctor__name">MARNIE TOLLER</p>
      <p class="doctor__credentials">D.C., Dipl. Ac. ASA</p>
    </div>

    <ul class="contact">
      <li>
        <svg viewBox="0 0 24 24" aria-hidden="true"><path d="M6.6 10.8a15.1 15.1 0 0 0 6.6 6.6l2.2-2.2a1 1 0 0 1 1-.25 11.4 11.4 0 0 0 3.6.57 1 1 0 0 1 1 1V20a1 1 0 0 1-1 1A17 17 0 0 1 3 4a1 1 0 0 1 1-1h3.5a1 1 0 0 1 1 1c0 1.25.2 2.45.57 3.6a1 1 0 0 1-.25 1z"/></svg>
        620-555-0147
      </li>
      <li>
        <svg viewBox="0 0 24 24" aria-hidden="true"><path d="M2 9l10-7 10 7v12H2zm2 1.2V19h16v-8.8l-8 5.3z"/></svg>
        drmarnie@solacegrove.com
      </li>
      <li>
        <svg viewBox="0 0 24 24" aria-hidden="true"><path d="M12 2a10 10 0 1 0 0 20 10 10 0 0 0 0-20zm0 2a8 8 0 0 1 6.9 4H15l-1.5 2-2.5-1-2 2 1 3 3 1v3l-2 2.9A8 8 0 0 1 5 7.5l2 2.5 2-1V6l3-2z"/></svg>
        solacegrove.net
      </li>
    </ul>

    <address class="address">
      584 W 12th St, Ste 320<br>
      Marlow Bend, KS 67419
    </address>
    <div class="accent-bar"></div>
  </section>

  <section class="card card--back" aria-label="Card back">
    <div class="practice-name">
      <span class="practice-name__main">Solace</span>
      <span class="practice-name__sub">Chiropractic &amp; Acupuncture</span>
    </div>
  </section>

</main>
</body>
</html>
```